Business Card Design Project

Use our current logo. Clean design.

Industry/Entity Type

Business

Requirements
Must have
• Marisela DUBRANCQ
M. Law
Managing Partner

Alpenvorsa AG
Kornhalmweg 214
CH-3097 Liebefeld

M. +41 79 412 56 27
T. +41 31 928 44 10
F. +41 31 928 44 19

m.dubrancq@alpenvorsa-example.com
www.alpenvorsa-example.com

```html
<!DOCTYPE html>
<html lang="en">
<head>
<meta charset="utf-8">
<title>Alpenvorsa AG – Business Card</title>
<link rel="stylesheet" href="https://fonts.googleapis.com/css2?family=Arimo:wght@400;700&display=swap">
<style>
  :root {
    --bg: #e4e4e4;
    --paper: #ffffff;
    --brand-red: #dc0a18;
    --ink: #1a1a1a;
    --card-w: 640px;
    --card-h: 414px;
  }
  * { box-sizing: border-box; margin: 0; padding: 0; }
  html, body {
    width: 1200px;
    height: 960px;
    overflow: hidden;
    background: var(--bg);
    font-family: "Arimo", Arial, sans-serif;
    color: var(--ink);
  }
  .sheet {
    width: 1200px;
    height: 960px;
    display: flex;
    flex-direction: column;
    align-items: center;
    justify-content: center;
    gap: 44px;
  }
  .card {
    position: relative;
    width: var(--card-w);
    height: var(--card-h);
    background: var(--paper);
    box-shadow: 0 6px 18px rgba(0,0,0,0.12);
  }

  /* Front side */
  .card--front { padding: 18px; }
  .front-field {
    position: relative;
    width: 100%;
    height: 100%;
    background: var(--brand-red);
    color: var(--paper);
  }
  .front-web {
    position: absolute;
    top: 40px;
    left: 0;
    right: 0;
    text-align: center;
    font-size: 13px;
    letter-spacing: 2.5px;
  }
  .front-name {
    position: absolute;
    left: 0;
    right: 0;
    top: 50%;
    transform: translateY(-40%);
    text-align: center;
    font-size: 58px;
    font-weight: 400;
    letter-spacing: 3px;
  }

  /* Back side */
  .brand {
    position: absolute;
    left: 58px;
    top: 180px;
    width: 250px;
    text-align: center;
    font-size: 30px;
    font-weight: 400;
    letter-spacing: 2px;
    color: var(--ink);
  }
  .details {
    position: absolute;
    left: 402px;
    top: 72px;
    width: 214px;
  }
  .name-band {
    background: var(--brand-red);
    color: var(--paper);
    font-weight: 700;
    font-size: 15px;
    letter-spacing: 0.6px;
    padding: 6px 8px;
    text-transform: uppercase;
  }
  .role {
    font-size: 10.5px;
    line-height: 14px;
    text-transform: uppercase;
    padding: 6px 8px 5px;
  }
  .rule { height: 3px; background: var(--brand-red); }
  .rule--gap { margin-top: 50px; }
  .address, .contact {
    font-size: 12.5px;
    line-height: 16px;
    padding: 10px 8px 0;
  }
  .contact { padding-top: 6px; }
  .contact-row { display: flex; line-height: 21px; }
  .contact-row dt { width: 28px; }
  .email { font-size: 12px; padding: 4px 0 6px 4px; white-space: nowrap; }
</style>
</head>
<body>
<main class="sheet">
  <section class="card card--front" aria-label="Card front">
    <div class="front-field">
      <p class="front-web">www.alpenvorsa-example.com</p>
      <p class="front-name">ALPENVORSA</p>
    </div>
  </section>

  <section class="card card--back" aria-label="Card back">
    <p class="brand">ALPENVORSA</p>
    <div class="details">
      <h1 class="name-band">Marisela Dubrancq</h1>
      <p class="role">M. Law<br>Managing Partner</p>
      <div class="rule"></div>
      <div class="rule rule--gap"></div>
      <address class="address" style="font-style:normal">
        Alpenvorsa AG<br>Kornhalmweg 214<br>CH-3097 Liebefeld
      </address>
      <dl class="contact">
        <div class="contact-row"><dt>M:</dt><dd>+41 79 412 56 27</dd></div>
        <div class="contact-row"><dt>T:</dt><dd>+41 31 928 44 10</dd></div>
        <div class="contact-row"><dt>F:</dt><dd>+41 31 928 44 19</dd></div>
      </dl>
      <p class="email">m.dubrancq@alpenvorsa-example.com</p>
      <div class="rule"></div>
    </div>
  </section>
</main>
</body>
</html>
```